Product Label Design

Need a product design for our Epsom salt product, needs to have a luxurious simple feel to it. The picture attached is our brand and wordage on it, the bag we think should be a stand up bag that should be offwhite/creme color. The other picture are products that we like. We updated the packaging to be a Kraft tube box, please see the attached photo for dimensions.

```html
<!DOCTYPE html>
<html lang="en">
<head>
<meta charset="utf-8">
<title>KAVRO Revive – Epsom Salt Pouch Label</title>
<link rel="stylesheet" href="https://fonts.googleapis.com/css2?family=Montserrat:wght@600;700;800&display=swap">
<style>
  :root {
    --backdrop: #e6cd86;
    --pouch: #f6e7b4;
    --pouch-light: #f8ecc2;
    --pouch-edge: #ecd89a;
    --seal-line: #dcc688;
    --ink: #1b1a36;
    --band: #141414;
    --band-text: #f6f1e2;
  }
  * { margin: 0; padding: 0; box-sizing: border-box; }
  html, body {
    width: 1200px;
    height: 960px;
    overflow: hidden;
  }
  body {
    background: var(--backdrop);
    font-family: "Montserrat", sans-serif;
    color: var(--ink);
    display: flex;
    align-items: center;
    justify-content: center;
  }
  .pouch {
    position: relative;
    width: 600px;
    height: 880px;
    background: linear-gradient(180deg, var(--pouch) 0%, var(--pouch-light) 45%, var(--pouch-edge) 100%);
    border-radius: 14px;
    box-shadow: 0 18px 40px rgba(120, 90, 20, 0.25);
  }
  .pouch__seal {
    position: absolute;
    left: 28px;
    right: 28px;
    height: 3px;
    background: var(--seal-line);
    border-radius: 2px;
  }
  .pouch__seal--top { top: 70px; }
  .pouch__seal--second { top: 78px; height: 2px; }
  .pouch__notch {
    position: absolute;
    top: 36px;
    width: 10px;
    height: 12px;
    background: var(--backdrop);
  }
  .pouch__notch--left { left: 0; border-radius: 0 6px 6px 0; }
  .pouch__notch--right { right: 0; border-radius: 6px 0 0 6px; }

  .label__line {
    position: absolute;
    left: 0;
    right: 0;
    text-align: center;
  }
  .label__brand {
    top: 226px;
    font-weight: 800;
    font-size: 88px;
    line-height: 1;
    letter-spacing: 1px;
  }
  .label__variant {
    top: 360px;
    font-weight: 700;
    font-size: 48px;
    line-height: 1;
    letter-spacing: 1px;
  }
  .label__product {
    top: 450px;
    font-weight: 600;
    font-size: 25px;
    line-height: 1.25;
  }
  .label__botanicals {
    top: 530px;
  }
  .label__band {
    display: inline-flex;
    gap: 38px;
    padding: 4px 8px;
    background: var(--band);
    color: var(--band-text);
    font-weight: 600;
    font-size: 24px;
    line-height: 1.2;
    border-radius: 2px;
  }
  .net-weight {
    position: absolute;
    bottom: 74px;
    left: 0;
    right: 0;
    text-align: center;
    font-weight: 600;
    font-size: 21px;
  }
</style>
</head>
<body>
  <main class="pouch">
    <span class="pouch__notch pouch__notch--left"></span>
    <span class="pouch__notch pouch__notch--right"></span>
    <span class="pouch__seal pouch__seal--top"></span>
    <span class="pouch__seal pouch__seal--second"></span>

    <h1 class="label__line label__brand">KAVRO</h1>
    <h2 class="label__line label__variant">REVIVE</h2>
    <p class="label__line label__product">US Sourced Pure Epsom Salt<br>(Magnesium Sulfate)</p>
    <p class="label__line label__botanicals"><span class="label__band"><span>+ Abies sibirica</span><span>+ Fir Balsam</span></span></p>

    <p class="net-weight">NET WT. 5LBS (1360g)</p>
  </main>
</body>
</html>
```